πΈ Full Website Redesign on Wix β The Harwick Pantry (Feminine, Sophisticated, Nature-Inspired)
Business Name: The Harwick Pantry
Current Site: https://lynkfold.example/Qr7tMwp (for structure reference only)
Platform: Wix
Business Type: Women-led Canadian online retail business
Location: Canada
π About The Harwick Pantry
The Harwick Pantry is a boutique e-commerce store specializing in roses and blooming plants, created for modern plant lovers who appreciate beauty, quality, and storytelling.
We are a small, women-led business in Ontario, Canada, and our audience is primarily women who are drawn to floral aesthetics, a calming user experience, and elevated design.
Our name β The Harwick Pantry β represents both a curated collection of blooms and a love of thoughtful, meaningful beauty.
π» Project Overview
We are looking for a full website redesign from scratch (built on Wix) that reflects our brand identity: feminine, sophisticated, romantic, and grounded in nature.
The current version of the site was just a test layout β we now want a fresh, cohesive design vision that speaks directly to our female Canadian customer base with a clean, modern, and elegant interface.
This project is not just about functionality β itβs about crafting an experience that feels like a digital floral sanctuary.
π― What We Need
Full website design and development in Wix (you can start fresh)
Custom homepage design with storytelling and a welcoming brand vibe
Pages to include (subject to refinement):
Home
Shop (products will be added by us later)
About
Contact
FAQ / Info
Blog or Guides (optional placeholder)
Sophisticated visual branding:
Muted rose, blush, and earthy tones
Clean, modern layout with elegant typography
Feminine, natural, soft design elements (think floral details, soft lines, minimalism with warmth)
Optimized for both desktop and mobile
Set up global styles (font, color palette, button styles, etc.)
Guidance or setup for product sections using Wixβs eCommerce system
Create beautiful reusable sections (for us to duplicate later as needed)
π· Brand Style
We are aiming for a website that feels like:
A curated botanical boutique
Feminine and warm β but not overly girly
Sophisticated and soft, never cluttered
Clean but not sterile
Relaxed elegance with a focus on natural beauty
Color palette:
Muted rose
Warm blush tones
Cream, soft beige, earthy sage
Very subtle contrast β no stark black-and-white
Typography:
Elegant serif or soft sans-serif pairings
Easy to read but with character
π Technical Info
Platform: Wix
No custom coding required (Wix-native tools preferred)
We will handle product uploads
Weβll provide any imagery you request
π¦ Deliverables
Fully designed Wix website (ready to publish)
All pages complete with consistent design and layout
Mobile-responsive layout
Design system set up for future content (colors, typography, etc.)
Optional: Style guide PDF for brand reference (bonus)
π Timeline
Weβd like the website to be completed within 1-2 weeks after project start. Please let us know your availability.
β
To Apply
Please include:
Portfolio (especially if youβve done Wix, floral, feminine, or nature-inspired work)
A short message on how you'd approach this project
Timeline/availability
We're looking for someone who understands how to design for emotion, beauty, and ease β not just functionality. If you love soft colors, delicate details, and creating meaningful digital experiences for women, we'd love to hear from you.
πΈ Letβs build something beautiful together!
Target Market(s)
Rose enthusiasts
Coding
Coded - Design and coding required
Number of Pages Required
5+ page

```html
<!DOCTYPE html>
<html lang="en">
<head>
<meta charset="utf-8">
<title>The Harwick Pantry — Home</title>
<link href="https://fonts.googleapis.com/css2?family=Marcellus&family=Poppins:wght@300;400;500&display=swap" rel="stylesheet">
<style>
:root{
  --plum:#4a2b40;
  --ink:#2b2b2b;
  --muted:#555;
  --sage:#8f9f88;
  --rose:#c58d8d;
  --rose-text:#cf9a9a;
  --cream:#fbf2e1;
  --line:#e4e4e4;
  --white:#fff;
}
*{box-sizing:border-box;margin:0;padding:0}
html,body{width:1200px;height:4598px;overflow:hidden;background:var(--white)}
body{font-family:"Poppins",sans-serif;color:var(--ink);position:relative}
.serif{font-family:"Marcellus",serif;font-weight:400}
section,header,footer{position:absolute;left:0;width:1200px}
.btn{display:inline-flex;align-items:center;justify-content:center;border-radius:30px;color:var(--white);font-family:"Marcellus",serif;font-size:19px;letter-spacing:.5px}
.btn-sage{background:var(--sage)}
.btn-rose{background:var(--rose)}
.ph{display:block}

/* header */
.site-header{top:0;height:146px}
.brand{position:absolute;left:75px;top:28px;display:flex;align-items:center;gap:16px}
.brand-square{width:57px;height:93px;border-radius:8px;background:var(--plum)}
.brand-name{font-family:"Marcellus",serif;font-size:29px;line-height:32px;color:var(--plum)}
.main-nav{position:absolute;left:352px;top:60px;display:flex;font-size:14px}
.main-nav a{color:var(--ink);text-decoration:none;margin-right:48px}
.main-nav a.active{border-bottom:1px solid var(--ink);padding-bottom:3px}
.header-icons{position:absolute;left:890px;top:64px;display:flex;gap:26px}
.cart{position:absolute;left:983px;top:50px;width:143px;height:48px;border-radius:24px;background:var(--sage);color:var(--white);font-size:15px;display:flex;align-items:center;justify-content:center;gap:8px}

/* hero */
.hero{top:146px;height:574px;background:linear-gradient(180deg,#4a4238 0%,#5b5245 45%,#3e3a31 100%);text-align:center;color:var(--white)}
.hero-kicker{position:absolute;top:140px;width:100%;font-size:54px;letter-spacing:3px}
.hero-title{position:absolute;top:190px;width:100%;font-size:80px;letter-spacing:4px}
.hero-sub{position:absolute;top:278px;width:100%;font-size:40px;letter-spacing:2px}
.hero .btn{position:absolute;left:479px;top:370px;width:241px;height:54px}
.dots{position:absolute;top:526px;left:565px;display:flex;gap:10px}
.dots i{width:10px;height:10px;border-radius:50%;background:var(--white)}
.dots i:first-child{background:var(--rose)}

/* collection */
.collection{top:720px;height:566px}
.section-title{font-size:34px;color:var(--ink)}
.collection .section-title{position:absolute;left:73px;top:60px}
.view-all{position:absolute;right:75px;top:68px;font-size:17px;color:var(--rose-text);text-decoration:underline}
.card{position:absolute;top:125px;width:245px;height:340px;border:1px solid var(--line);border-radius:8px;background:var(--white)}
.card.lift{box-shadow:0 4px 22px rgba(0,0,0,.14);border-color:transparent}
.card .ph{position:absolute;left:16px;top:15px;width:212px;height:231px;border-radius:4px}
.card h3{position:absolute;left:20px;top:268px;font-size:20px}
.card p{position:absolute;left:20px;top:300px;font-size:15px}

/* about */
.about{top:1286px;height:514px;background:var(--cream)}
.about .ph{position:absolute;left:0;top:0;width:586px;height:514px}
.about-body{position:absolute;left:615px;top:60px;width:500px}
.about-body h2{font-size:34px;margin-bottom:22px}
.about-body p{font-size:13.5px;line-height:27px;color:var(--muted);margin-bottom:10px}
.about-body .btn{width:182px;height:56px;margin-top:18px}

/* journey */
.journey{top:1800px;height:697px}
.journey-body{position:absolute;left:73px;top:160px;width:420px}
.journey-body h2{font-size:34px;line-height:39px;margin-bottom:24px}
.journey-body p{font-size:13.5px;line-height:27px;color:var(--muted)}
.journey-body .btn{width:182px;height:56px;margin-top:32px}
.journey .ph{position:absolute;left:523px;top:90px;width:606px;height:523px;border-radius:6px}

/* newsletter */
.newsletter{top:2497px;height:503px;background:linear-gradient(180deg,#6f7c63,#7a8769 55%,#6b7860);text-align:center;color:var(--white)}
.newsletter h2{position:absolute;top:115px;width:100%;font-size:48px;line-height:48px;letter-spacing:2px}
.newsletter .offer{position:absolute;top:230px;width:100%;font-size:29px;letter-spacing:1px}
.signup{position:absolute;left:229px;top:317px;display:flex}
.signup .field{width:620px;height:58px;background:var(--white);color:var(--ink);font-size:15px;display:flex;align-items:center;padding-left:18px}
.signup .btn{width:126px;height:58px;border-radius:0 30px 30px 0}

/* blog */
.blog{top:3000px;height:684px;text-align:center}
.blog h2{position:absolute;top:70px;width:100%;font-size:34px}
.blog .lede{position:absolute;top:136px;width:100%;font-size:17px}
.post{position:absolute;top:188px;width:331px;text-align:left}
.post .ph{width:331px;height:205px;border-radius:4px}
.post time{display:block;font-size:13px;margin-top:18px}
.post h3{font-size:21px;line-height:27px;margin-top:6px;color:var(--ink)}
.blog .btn{position:absolute;left:510px;top:560px;width:181px;height:54px}

/* social gallery */
.gallery{top:3684px;height:491px;background:var(--cream);text-align:center}
.gallery h2{position:absolute;top:50px;width:100%;font-size:34px}
.gallery-grid{position:absolute;left:74px;top:118px;display:flex;gap:13px}
.gallery-grid .ph{width:254px;height:215px;border-radius:4px}
.gallery .btn{position:absolute;left:468px;top:378px;width:264px;height:54px}

/* footer */
.site-footer{top:4175px;height:423px}
.site-footer .brand{left:75px;top:118px}
.footer-col{position:absolute;top:60px}
.footer-col h4{font-family:"Marcellus",serif;font-weight:400;font-size:21px;color:var(--rose-text);margin-bottom:10px}
.footer-col li{list-style:none;font-size:14px;line-height:32px}
.footer-rule{position:absolute;left:0;top:357px;width:1200px;border-top:1px solid var(--line)}
.copyright{position:absolute;left:73px;top:385px;font-size:12px;color:var(--muted)}
.social{position:absolute;left:955px;top:382px;display:flex;gap:22px}
.social i{width:20px;height:20px;border-radius:50%;background:var(--ink)}
</style>
</head>
<body>

<header class="site-header">
  <div class="brand"><span class="brand-square"></span><span class="brand-name">The Harwick<br>Pantry</span></div>
  <nav class="main-nav">
    <a class="active">Home</a><a>About Us</a><a>Shop</a><a>FAQ</a><a>Blog</a><a>Contact</a>
  </nav>
  <div class="header-icons">
    <svg width="16" height="16" viewBox="0 0 16 16" fill="none" stroke="#222" stroke-width="2"><circle cx="7" cy="7" r="5"/><path d="M11 11l4 4"/></svg>
    <svg width="16" height="16" viewBox="0 0 16 16" fill="none" stroke="#222" stroke-width="1.5"><circle cx="8" cy="5" r="3.5"/><path d="M1.5 15c0-3.5 3-5.5 6.5-5.5s6.5 2 6.5 5.5z"/></svg>
  </div>
  <div class="cart">
    <svg width="16" height="14" viewBox="0 0 16 14" fill="#fff"><path d="M1 5h14l-2 8H3z"/><path d="M4 5l3-4M12 5L9 1" stroke="#fff" stroke-width="1.5"/></svg>
    $0.00(0)
  </div>
</header>

<section class="hero" role="img" aria-label="Interior of a plant boutique with hanging lamps and shelves of potted plants">
  <div class="hero-kicker serif">WELCOME TO</div>
  <h1 class="hero-title serif">THE HARWICK PANTRY</h1>
  <p class="hero-sub serif">Potted Beauty, Ready to Root at Home.</p>
  <a class="btn btn-sage">Show Now</a>
  <div class="dots"><i></i><i></i><i></i><i></i></div>
</section>

<section class="collection">
  <h2 class="section-title serif">Explore the Collection</h2>
  <a class="view-all">View all collections</a>
  <article class="card" style="left:73px"><span class="ph" role="img" aria-label="Yellow roses in bloom" style="background:linear-gradient(135deg,#e9c84a,#6d7a3d)"></span><h3 class="serif">Amberly Blush</h3><p>C$31.99</p></article>
  <article class="card" style="left:345px"><span class="ph" role="img" aria-label="Pale peach climbing roses" style="background:linear-gradient(135deg,#e8cbb8,#7f8d5c)"></span><h3 class="serif">Amberly Blush</h3><p>C$31.99</p></article>
  <article class="card lift" style="left:616px"><span class="ph" role="img" aria-label="Single orange rose bloom" style="background:radial-gradient(circle at 50% 45%,#f2875a,#e05f3a 55%,#2f3a2a)"></span><h3 class="serif">Amberly Blush</h3><p>C$31.99</p></article>
  <article class="card" style="left:884px"><span class="ph" role="img" aria-label="Orange roses on a leafy bush" style="background:linear-gradient(135deg,#e89a2c,#3f5a2a)"></span><h3 class="serif">Amberly Blush</h3><p>C$31.99</p></article>
</section>

<section class="about">
  <span class="ph" role="img" aria-label="Two shop owners standing among potted plants" style="background:linear-gradient(135deg,#3c4a33,#7a6a58 50%,#c07a5a)"></span>
  <div class="about-body">
    <h2 class="serif">About The Harwick Pantry</h2>
    <p>The Harwick Pantry is a boutique e-commerce store specializing in roses and blooming plants, created for modern plant lovers who appreciate beauty, quality, and storytelling.</p>
    <p>We are a small, women-led business in Ontario, Canada, and our audience is primarily women who are drawn to floral aesthetics, a calming user experience, and elevated design.</p>
    <p>Our name — The Harwick Pantry — represents both a curated collection of blooms and a love of thoughtful, meaningful beauty.</p>
    <a class="btn btn-rose">Learn More</a>
  </div>
</section>

<section class="journey">
  <div class="journey-body">
    <h2 class="serif">Our Journey from Seed<br>to Blossom</h2>
    <p>The Harwick Pantry is dedicated to providing a curated collection of roses and blooming plants, carefully selected to bring joy and elegance to your home garden. Our team is committed to sharing our passion for plants and fostering a community of plant enthusiasts. Join us in celebrating the beauty of nature and the art of plant care.</p>
    <a class="btn btn-rose">Learn More</a>
  </div>
  <span class="ph" role="img" aria-label="Close-up of a dandelion seed head" style="background:radial-gradient(circle at 50% 48%,#e6e8e0,#9fae9c 40%,#56695c)"></span>
</section>

<section class="newsletter" role="img" aria-label="Blurred background of plants on a wooden table">
  <h2 class="serif">Stay Informed About Plants and More.<br>No Spam, We Promise.</h2>
  <p class="offer serif">Subscribe Now and Enjoy 15% Off Your First Purchase</p>
  <div class="signup"><div class="field">Enter Email Address</div><a class="btn btn-rose">Submit</a></div>
</section>

<section class="blog">
  <h2 class="serif">The Harwick Guide: Our Plant Care Blog</h2>
  <p class="lede">Your Source for Plant Care Tips and Advice</p>
  <article class="post" style="left:73px"><span class="ph" role="img" aria-label="Potted houseplants on a windowsill" style="background:linear-gradient(135deg,#7aa05a,#3d4d30)"></span><time>Aug 06, 2025</time><h3 class="serif">Nemo enim ipsam voluptatem quia voluptas..</h3></article>
  <article class="post" style="left:436px"><span class="ph" role="img" aria-label="Shopping cart filled with red flowers in a store" style="background:linear-gradient(135deg,#8a6a5a,#b34a45 50%,#7a8a80)"></span><time>Aug 06, 2025</time><h3 class="serif">Nemo enim ipsam voluptatem quia voluptas..</h3></article>
  <article class="post" style="left:797px"><span class="ph" role="img" aria-label="Plant shop interior with shelves of greenery" style="background:linear-gradient(135deg,#6f7a55,#b09a78)"></span><time>Aug 06, 2025</time><h3 class="serif">Nemo enim ipsam voluptatem quia voluptas..</h3></article>
  <a class="btn btn-rose">View All Blog</a>
</section>

<section class="gallery">
  <h2 class="serif">Join Us on Petalgram</h2>
  <div class="gallery-grid">
    <span class="ph" role="img" aria-label="Hands holding a glossy leafed plant" style="background:linear-gradient(135deg,#e9e6df,#2f3a28)"></span>
    <span class="ph" role="img" aria-label="Bright room with potted plants on a ladder shelf" style="background:linear-gradient(135deg,#efe7da,#a08a66)"></span>
    <span class="ph" role="img" aria-label="Two women reviewing a tablet among plants" style="background:linear-gradient(135deg,#3e4a36,#b8775a)"></span>
    <span class="ph" role="img" aria-label="Ceramic planters with cactus and succulents" style="background:linear-gradient(135deg,#2c3a2a,#d8d2c6)"></span>
  </div>
  <a class="btn btn-sage">Follow Us on Petalgram</a>
</section>

<footer class="site-footer">
  <div class="brand"><span class="brand-square"></span><span class="brand-name">The Harwick<br>Pantry</span></div>
  <div class="footer-col" style="left:391px"><h4>Navigations</h4><ul><li>Home</li><li>About Us</li><li>Shop</li><li>FAQ</li><li>Blog</li><li>Contact</li></ul></div>
  <div class="footer-col" style="left:637px"><h4>My Account</h4><ul><li>Shop All</li><li>Plants</li><li>Pots</li><li>Sale</li><li>Gift Card</li><li>Subscriptions</li><li>Care</li></ul></div>
  <div class="footer-col" style="left:884px"><h4>Helpful Links</h4><ul><li>FAQ</li><li>Shipping &amp; Returns</li><li>Terms &amp; Conditions</li><li>Payment Methods</li></ul></div>
  <div class="footer-rule"></div>
  <p class="copyright">Copyright © 2025 Company Name All rights reserved.</p>
  <div class="social" aria-label="Social links"><i></i><i></i><i></i><i></i><i></i></div>
</footer>

</body>
</html>
```